Coffee Company 1lb coffee bag design

Coffee Bag Design Size ( bag size 12 -16oz / 340 -454 grams / 1lb - dimensions) THE BAG IS GUSSETTED - meaning it has 4sides , like the bags shown in the attachments

* recommend text located at the bottom of the brief added July 9 th

We need a design for a retail 1lb coffee bag to package our Artisan handcrafted roasted coffee beans. The design we choose will be the standard 'look' for our freshly roasted coffee. We have our logo and need to incorporate that into an original, overall design that includes areas for text boxes on the front, back and sides. We have provided a draft of the text at the bottom of the brief to be incorporated in the design. One text box on the front will remain blank. This is where we will adhere a label that will describe the particular coffee in the package. And blank text box on the back to print a bar code.
(Side of the bag : one side of the bag would be our company story (details can be found on our web site) and the other side panel brewing instruction. I would be able to provide the txt for the 'story' and 'brewing instructions' as needed)

These are our preliminary thoughts and are open minded to other options.
We want the design to convey that our coffee is an ethically sourced , locally hand roasted in small batches , freshly roasted, sustainable, socially and environmentally responsible.

This bag will be the our main core bag for use with all the Blends / Roasts so it will need to be starting point for our overall bag design branding. We are very open to all and any creative ideas..
Ideally we would like to use a crisp white gloss bag - the logo would be the main focal point with an area below for where we would place our sticker - roast / blend details .we will be to using a sticker on the front of the bag to identify the various roasts / blends we offer until a point of having a different bag for each coffee. We don't want the bag the appear 'busy' as we prefer images over covering the whole bag with a photo.. the design needs to be crisp , clean , not overall busy, classy , using inspiration perhaps from the logo , harrow mountain range , blue ocean, green trees .... our customers enjoy the finer things in life and our brand is more of a luxury product.
Who we are:
We are a Artisan coffee roaster located in the village of Fernhollow. Our hand crafted roasted coffee is ethically sourced , locally roasted in small batches to ensure freshness in every cup. please check out our web site for further details on the company. Again , we are open and looking forward to seeing some fantastic core bag design. we will be looking for the opportunity to develop stickers for each blends in the future...

www.fernhollowcoffeeco.example

attached is the logo files and other bags that have caught our interest ... have some fun!

TEXT FOR: SIDE #1, SIDE #2 , BACK OF THE BAG

FYI - this text is still currently in DRAFT but will allow us to get an overall look for each design...

One side of the coffee bag

Revised draft of the text - updated July19th

THE STORY OF

THE FERNHOLLOW

COFFEE COMPANY,

Nestled beneath the two majestic peaks of The Harrow mountains along the scenic Cedar Reach highway, is the picturesque village of Fernhollow. This small waterfront community on Vancouver’s North Shore boasts a synchronicity between snowcapped mountains that feed twinkling creeks which meander through lush green forests and lead to the beautiful ocean. This was our inspiration to create Fernhollow Coffee Company and to share our passion for the perfect cup of coffee as reflected in each of our roasts. Our artisan roasted coffee is ethically sourced, using the highest quality Arabica beans then locally roasted in small batches to ensure freshness and the finest flavor. May the coffee you are about to enjoy, enhance your day as you experience the essence of Fernhollow.

-------------------------------------------------

Fernhollow Coffee Company

PO BOX 862

Fernhollow BC

V0N 4K7

the other Side of Bag

KEYS TO BREWING

THE PERFECT CUP

FRESHNESS

Always use freshly roasted (Fernhollow Coffee Company)

beans and within 1-2 weeks of purchase.

STORING

Your coffee has 4 enemies:

Heat, Moisture, Light & Air

Keep your coffee cool, dry and dark in an

airtight container for maximum flavour.

GRINDING

Grind beans just before

brewing. Select the best

grind for each brewing method:

Espresso = Finer Grind

Filtered = Medium Grind

French Press = Coarse Grind

BREWING

Water I Ratio I Temperature

Water: Fresh, cold, filtered water

Ratio: Use 2 rounded tablespoons

of coffee per 8 oz of water.

Temperature: Heat water between 90 – 96 C

Adjust brewing methods to your personal taste.

For more information about

brewing the perfect cup of coffee,

visit our website at

www.fernhollowcoffeeco

(ADD RBGT logo - to be provided)

Back of the bag

"The roasts I create for Fernhollow Coffee Company are a reflection of my commitment to craft the perfect cup of coffee. I hope it is the finest coffee you'll ever enjoy."
- Doran Whitlock,
Founder & Master Roaster, Fernhollow Coffee Company

Visit us our website to learn more including ordering your freshly roasted coffees

(ADD miniature Fernhollow Coffee Company logo)

Like us on Facebook

htpp://www.facebook.com/fernhollowcoffeeco

Follow us on Chirper

Fernhollow Coffee @fernhollowbrew

send us an email

info@fernhollowcoffeeco.example
Updates

Design Team, just a reminder the bag design is for a gusseted bag ( see brief for details and images ) and not for a pouch bag as what is being submitted to me ? All current designs received so far are the wrong style of bag.

Update effective July 19th, 2014. Please see Brief for revised text for Keys to Brewing, The Story and back side of bag. Thanks.

Reason: Still working with a few designers with text and design - need more time Starting to narrow our selection down soon

Reason: Need to extend to add French to package design

Target Market(s)

coffee drinkers with a mature palate for Arabica Beans , ethically sourced

Font styles to use
Other font styles liked:
• same font as logo ?

Colors
0893cd
33a6d7
85cae6
85acd3
3176b5
0455a3
ffffff
cee9f5
eaf1f6

Requirements
Must have
• logo is the main image on front of bag , space for the sticker that will describe the type of bean / roast / blend
Nice to have
• white bag , logo has strong presents front and middle of the bag. crisp clean not busy designs
Should not have
• package should not be 'too busy' it is the core for all roasts and should stand for the roasting company

no cartoon pictures and un authorized clip art

```html
<!DOCTYPE html>
<html lang="en">
<head>
<meta charset="utf-8">
<title>Fernhollow Coffee Company – 1 lb Gusseted Bag Dieline</title>
<link rel="stylesheet" href="https://fonts.googleapis.com/css2?family=Noticia+Text:wght@400;700&family=Quicksand:wght@700&display=swap">
<style>
  :root {
    --flap-grey: #666666;
    --panel-white: #ffffff;
    --rule: #1a1a1a;
    --ink: #1a1a1a;
    --accent-cyan: #4cc8ef;
    --mountain-light: #d6f0fa;
    --mountain-mid: #9fdcf2;
    --brand-brown: #3a2a20;
  }
  html, body {
    margin: 0;
    padding: 0;
    width: 1200px;
    height: 1054px;
    overflow: hidden;
    background: var(--panel-white);
  }
  .dieline {
    position: relative;
    width: 1139px;
    height: 1000px;
    transform: scale(1.0536, 1.054);
    transform-origin: 0 0;
    font-family: "Noticia Text", Georgia, serif;
    color: var(--ink);
  }
  .dieline-shapes {
    position: absolute;
    inset: 0;
  }
  .flap { fill: var(--flap-grey); }
  .panel { fill: var(--panel-white); stroke: var(--rule); stroke-width: 1; }

  .panel-heading {
    position: absolute;
    margin: 0;
    font-family: "Quicksand", "Arial Rounded MT Bold", sans-serif;
    font-weight: 700;
    font-size: 17px;
    letter-spacing: 3px;
    color: var(--accent-cyan);
    text-align: center;
    text-transform: uppercase;
  }
  .copy p { margin: 0 0 14px; }

  /* Side panel: story */
  .story-heading { left: 57px; width: 190px; top: 118px; }
  .story-copy {
    position: absolute;
    left: 63px; top: 158px; width: 178px;
    font-size: 11.3px; line-height: 13.7px;
    letter-spacing: -0.2px;
    text-align: center;
  }

  /* Front panel */
  .brand-mark {
    position: absolute;
    left: 255px; top: 40px; width: 307px; height: 320px;
    display: flex; flex-direction: column; align-items: center; justify-content: center;
    gap: 22px;
  }
  .brand-dot {
    width: 110px; height: 110px; border-radius: 50%;
    background: var(--brand-brown);
  }
  .brand-name {
    margin: 0;
    font-weight: 700;
    font-size: 26px;
    line-height: 32px;
    color: var(--brand-brown);
    text-align: center;
  }
  .mountain-range {
    position: absolute;
    background: linear-gradient(180deg, var(--mountain-light) 0%, var(--mountain-mid) 100%);
  }
  .mountain-range.front { left: 248px; top: 365px; width: 321px; height: 111px; }
  .mountain-range.back  {
    left: 761px; top: 372px; width: 321px; height: 210px;
    background: linear-gradient(180deg, rgba(214,240,250,0.7) 0%, rgba(214,240,250,0.2) 100%);
  }
  .product-band {
    position: absolute;
    left: 248px; top: 476px; width: 321px; height: 42px;
    background: var(--accent-cyan);
    color: var(--panel-white);
    font-family: "Quicksand", "Arial Rounded MT Bold", sans-serif;
    font-weight: 700; font-size: 14px; line-height: 17px;
    letter-spacing: 2px; text-align: center;
    display: flex; align-items: center; justify-content: center;
  }
  .net-weight {
    position: absolute;
    left: 260px; top: 718px;
    margin: 0;
    font-weight: 700; font-size: 14px; line-height: 17px;
  }

  /* Side panel: brewing */
  .brewing-heading { left: 570px; width: 190px; top: 112px; }
  .brewing-copy {
    position: absolute;
    left: 578px; top: 151px; width: 176px;
    font-size: 11.6px; line-height: 14.4px;
    letter-spacing: -0.1px;
  }
  .brewing-copy p { margin-bottom: 13px; }

  /* Back panel */
  .back-copy {
    position: absolute;
    left: 780px; top: 122px; width: 286px;
    font-size: 10.6px; line-height: 12.6px;
  }
  .back-copy p { margin-bottom: 12px; }
  .web-address {
    font-family: "Quicksand", "Arial Rounded MT Bold", sans-serif;
    font-weight: 700; font-size: 11px;
    letter-spacing: 1.5px; font-variant: small-caps;
    color: var(--accent-cyan);
  }
</style>
</head>
<body>
<div class="dieline">
  <svg class="dieline-shapes" width="1139" height="1000" viewBox="0 0 1139 1000" aria-hidden="true">
    <polygon class="flap" points="57,0 0,60 0,700 57,757"/>
    <polygon class="flap" points="1083,0 1139,60 1139,700 1083,757"/>
    <polygon class="flap" points="57,757 247,757 247,770 185,810 110,810"/>
    <polygon class="flap" points="570,757 760,757 760,770 710,810 630,810 570,770"/>
    <polygon class="flap" points="760,757 1083,757 1083,770 1015,810 835,810 760,770"/>
    <polygon class="flap" points="247,762 200,825 200,945 247,1000"/>
    <polygon class="flap" points="570,762 618,825 618,945 570,1000"/>
    <rect class="panel" x="57" y="0.5" width="190" height="757"/>
    <rect class="panel" x="247" y="0.5" width="323" height="757"/>
    <rect class="panel" x="570" y="0.5" width="190" height="757"/>
    <rect class="panel" x="760" y="0.5" width="323" height="757"/>
    <rect class="panel" x="247" y="757" width="323" height="242.5"/>
  </svg>

  <!-- Side panel: company story -->
  <h2 class="panel-heading story-heading">Our Story</h2>
  <div class="copy story-copy">
    <p>Nestled beneath the two majestic peaks of The Harrow mountains along the scenic Cedar Reach highway, is the picturesque village of Fernhollow. This small waterfront community on Vancouver’s North Shore boasts a synchronicity between snow-capped mountains feeding twinkling creeks meandering through lush green forests and trails leading to the beautiful ocean and was the inspiration for Fernhollow Coffee Company.</p>
    <p>As a local coffee roaster, we know how important having the perfect cup of coffee is to get your day started, celebrating special occasions or just having a quiet moment to yourself. For this reason we source only the finest sustainable Arabica beans, roasting them in small batches and hand delivering them in state-of-the art packaging guaranteeing that your coffee is the freshest that it can be because you deserve it. You can feel good about enjoying every cup of Fernhollow Coffee because we ensure that we are choosing our beans ethically.</p>
    <p>We hope that you will be inspired by our roasts as much as we were inspired to create them.</p>
  </div>

  <!-- Front panel -->
  <div class="brand-mark">
    <div class="brand-dot"></div>
    <p class="brand-name">Fernhollow<br>Coffee Company</p>
  </div>
  <div class="mountain-range front" role="img" aria-label="Pale blue snow-capped mountain range illustration"></div>
  <div class="product-band">FRESH ROASTED<br>WHOLE BEAN COFFEE</div>
  <p class="net-weight">Net Weight: 16 oz (1 lb)<br>Poids Net: 454 g</p>

  <!-- Side panel: brewing tips -->
  <h2 class="panel-heading brewing-heading">Brewing Tips</h2>
  <div class="copy brewing-copy">
    <p>Patience will help you perfect your brew, but preparation is the key to insuring that perfection.</p>
    <p>Here are some basic, but important things to consider.</p>
    <p>1) Buy freshly roasted beans</p>
    <p>2) Store your beans properly. A cool, dry place in an airtight container. <strong>NOT</strong> the fridge or the freezer.</p>
    <p>3) Coffee should be used 3-4 weeks after roasting for optimal flavour.</p>
    <p>4) Size matters. Insure your grind is the right consistency for your brewing method. If you don't have a good grinder at home cheat and take your beans to your local barista.</p>
    <p>5) Keep your equipment clean.</p>
    <p>6) Filter your water. This has a huge impact on flavour.</p>
    <p>7) Ensure your water temperature is appropriate for your method, your grind and the roast you are using.</p>
  </div>

  <!-- Back panel -->
  <div class="mountain-range back" role="img" aria-label="Faint pale blue mountain range illustration"></div>
  <div class="copy back-copy">
    <p>Doran Whitlock returned to his home on the West Coast after enjoying an international career with a world-renowned coffee company and chose to settle his family in Fernhollow. He created Fernhollow Coffee Company to share his passion for the perfect cup and the beauty of his home as reflected in each of our roasts. This artisan coffee is ethically sourced, locally roasted in small batches and delivered in state-of-the-art packaging to ensure the freshest beans, highest quality and finest flavour. May the cup you are about to enjoy, enhance your day as you experience the essence of Fernhollow.</p>
    <p>We are proud members of the RBGT.</p>
    <p><strong>Inspire us:</strong> Submit a creative name for a special roast. If we use it, receive some free coffee—who doesn't like free?</p>
    <p>Follow us and our journey on Chirper:<br><strong>@fernhollowbrew</strong></p>
    <p class="web-address">FernhollowCoffeeCo.example</p>
  </div>
</div>
</body>
</html>
```